Website Design for a Project Management Consulting Business

I have a logo design already and now I need a website.
I am a project manager and run my own consulting business.
Currently I am under contract with 3 major Kestrelmark 300 companies. I'd like a website I can direct current and future clients.
My job is running IT projects and working with developers to deliver business priorities.
The website should be professional and clean - I work IT projects and would like to incorporate that into any theme.
I'd like the site to have several page or breakoff links - sections would include : about me, about my services, a page to display all of my certification badges, another page to talk about highlights from past projects and so on.
Looking for a collaborative experience.

Industry/Entity Type

Kestrelmark 300 Consulting Firm - Project Management

Coding

Coded - Design and coding required

Number of Pages Required

1 page

Font styles to use
Serif

Colors
0094D4
00A9DD
6FCCEA
C7EBF8
E9F6FB
EE7325
F08F49
F5BC92
FAE3D3
FDF4ED

Requirements
Must have
• Sections that are a must: About Me (bio), About My Services, About my Certifications and Credentials, Experience on Past Projects,
Nice to have
• I have added the logo below - I'd like to use the logo and have it prominent ; should be professional and inviting

```html
<!DOCTYPE html>
<html lang="en">
<head>
<meta charset="utf-8">
<title>Meridian Project Partners — Project Management Consulting</title>
<link href="https://fonts.googleapis.com/css2?family=Barlow:wght@400;500;600;700&family=Barlow+Condensed:wght@500;600;700&display=swap" rel="stylesheet">
<style>
:root{
  --navy:#0b3a63;
  --blue:#00a9dd;
  --blue-deep:#0094d4;
  --blue-pale:#e9f6fb;
  --blue-soft:#c7ebf8;
  --orange:#ee7325;
  --orange-lt:#f08f49;
  --ink:#2b2f36;
  --muted:#4a4f57;
  --footer:#f3f3f3;
  --cond:'Barlow Condensed', sans-serif;
  --body:'Barlow', sans-serif;
}
*{box-sizing:border-box;margin:0;padding:0}
html,body{width:1200px;height:3622px;overflow:hidden;background:#fff}
body{position:relative;font-family:var(--body);color:var(--ink)}
.abs{position:absolute}
.heading{font-family:var(--cond);font-weight:700;color:var(--navy);letter-spacing:.2px;line-height:1}
.heading .accent{color:var(--blue)}
.rule{position:absolute;width:42px;height:3px;background:var(--orange)}
.btn{position:absolute;display:flex;align-items:center;justify-content:center;border-radius:22px;
  background:linear-gradient(180deg,var(--orange-lt),var(--orange));color:#fff;font-family:var(--cond);
  font-weight:700;font-size:17px;letter-spacing:1.2px}
.photo{position:absolute;border-radius:50%}

/* header */
.brand{display:flex;align-items:center;gap:12px}
.brand-mark{width:48px;height:48px;background:var(--navy)}
.brand-name{font-family:var(--cond);font-weight:700;color:var(--navy);font-size:30px;line-height:1;letter-spacing:1px}
.topline{right:24px;top:18px;display:flex;gap:28px;font-family:var(--cond);font-weight:500;font-size:16px;color:var(--navy)}
.topline span{display:flex;align-items:center;gap:8px}
.nav{right:24px;top:61px;display:flex;gap:16px;font-size:12px;letter-spacing:1.3px;color:var(--navy);font-weight:500}
.nav a{color:inherit;text-decoration:none;display:flex;align-items:center;gap:8px}
.nav a::before{content:"";width:16px;height:1px;background:var(--navy)}

/* hero */
.hero-title{left:158px;top:218px;font-size:41px}
.hero-title .big{display:block;font-size:54px;color:var(--blue);margin-top:4px}
.hero-text{left:159px;top:330px;width:360px;font-size:18px;line-height:27px;color:var(--muted)}

/* services */
.center-head{left:0;width:1200px;text-align:center;font-size:48px}
.services{left:158px;top:753px;width:883px;height:232px;display:grid;grid-template-columns:289px 303px 291px;grid-template-rows:112px 120px}
.service{display:flex;align-items:center;justify-content:center;text-align:center;font-weight:700;font-size:18px;line-height:27px;color:var(--navy);letter-spacing:.3px}
.service.r1{border-bottom:2px solid var(--blue)}
.service.c2{border-left:2px solid var(--blue);border-right:2px solid var(--blue)}

/* about */
.about-title{left:644px;top:1104px;font-size:48px}
.about-text{left:644px;top:1190px;width:396px;font-size:15.5px;line-height:24px;color:var(--muted)}
.about-text p+p{margin-top:24px}
.stat{top:1452px;font-family:var(--cond)}
.stat b{display:block;font-size:34px;color:var(--orange);font-weight:600;line-height:1}
.stat span{display:block;font-size:17px;font-weight:600;color:var(--navy);margin-top:4px}

/* certifications */
.badge-row{left:210px;top:1812px;width:780px;height:90px}
.arrow{top:1835px}

/* trusted */
.trusted-title{left:159px;top:2038px;font-size:48px;line-height:58px}
.quote-mark{left:158px;top:2202px}
.quote{left:180px;top:2210px;width:380px;font-size:15.5px;line-height:24px;color:var(--muted)}
.quote-name{left:180px;top:2344px;font-weight:700;font-size:15px;color:var(--navy)}
.quote-role{left:180px;top:2368px;font-size:15px;color:var(--muted)}

/* experience */
.card-img{position:absolute;top:2596px;height:204px}
.card-title{position:absolute;top:2820px;text-align:center;font-family:var(--cond);font-weight:600;font-size:24px;line-height:28px;color:var(--navy)}

/* contact */
.contact-title{left:158px;top:2962px;font-size:48px}
.contact-text{left:158px;top:3056px;width:330px;font-size:15.5px;line-height:24px;color:var(--muted)}
.contact-line{left:158px;display:flex;align-items:flex-start;gap:12px;font-family:var(--cond);font-size:19px;color:var(--navy)}
.contact-line .lbl{width:72px;font-weight:500}
.contact-line .val{font-weight:500}
.field{position:absolute;border:2px solid var(--navy);border-radius:6px;font-family:var(--cond);font-size:14px;color:#6b7280;letter-spacing:.5px;padding:8px 14px}

/* footer */
.footer{left:0;top:3388px;width:1200px;height:234px;background:var(--footer)}
.foot-head{font-family:var(--cond);font-weight:700;font-size:20px;color:var(--navy)}
.foot-links{font-size:12.5px;line-height:24px;color:var(--ink);list-style:none}
.copyright{left:722px;top:3563px;font-size:12.5px;color:var(--ink)}
</style>
</head>
<body>

<!-- header -->
<div class="abs brand" style="left:22px;top:22px"><div class="brand-mark"></div><div class="brand-name">MERIDIAN</div></div>
<div class="abs topline">
  <span><svg width="16" height="16" viewBox="0 0 16 16"><path d="M4 2l2 3-1.5 1.5c.8 2 2.5 3.8 4.5 4.5L10.5 9.5l3 2-1 2.5C7 14 2 9 2 3.5z" fill="none" stroke="#ee7325" stroke-width="1.4"/></svg>Call Me - (555) 010-2468</span>
  <span><svg width="16" height="12" viewBox="0 0 16 12"><rect x="1" y="1" width="14" height="10" rx="1" fill="none" stroke="#ee7325" stroke-width="1.3"/><path d="M1 1l7 6 7-6" fill="none" stroke="#ee7325" stroke-width="1.3"/></svg>Emai Me - hello@meridianpartners.example</span>
</div>
<nav class="abs nav"><a>ABOUT ME</a><a>MY SERVICES</a><a>CERTIFICATIONS AND CREDENTIALS</a><a>EXPERIENCE</a><a>CONTACT</a></nav>

<!-- hero -->
<h1 class="abs heading hero-title">EXTENSIVE EXPERIENCED<span class="big">CONSULTANT</span></h1>
<p class="abs hero-text">Serves as Principal Lead Consultant on waterfall and agile contract opportunities.</p>
<div class="btn" style="left:159px;top:407px;width:183px;height:42px">MY EXPERIENCE</div>
<svg class="abs" style="left:590px;top:108px" width="460" height="470" viewBox="0 0 460 470">
  <circle cx="381" cy="75" r="68" fill="#f08f49"/>
  <circle cx="99" cy="398" r="59" fill="#00a9dd"/>
</svg>
<div class="photo" role="img" aria-label="Portrait photograph of the consultant in a pinstripe suit against a dark background" style="left:599px;top:114px;width:442px;height:442px;background:radial-gradient(circle at 55% 40%,#6b4a3a,#1c1a1a 70%)"></div>

<!-- services -->
<h2 class="abs heading center-head" style="top:656px">ABOUT <span class="accent">MY SERVICES</span></h2>
<div class="rule" style="left:579px;top:723px"></div>
<div class="abs services">
  <div class="service r1">LEADING SAFE AGILE<br>SCRUM TEAMS</div>
  <div class="service r1 c2">LEADING SAFE AGILE<br>SCRUM TEAMS</div>
  <div class="service r1">LEADING SAFE AGILE<br>SCRUM TEAMS</div>
  <div class="service">LEADING SAFE AGILE<br>SCRUM TEAMS</div>
  <div class="service c2">LEADING SAFE AGILE<br>SCRUM TEAMS</div>
  <div class="service">LEADING SAFE AGILE<br>SCRUM TEAMS</div>
</div>

<!-- about me -->
<svg class="abs" style="left:150px;top:1140px" width="460" height="200" viewBox="0 0 460 200">
  <circle cx="379" cy="77" r="70" fill="#00a9dd"/>
</svg>
<div class="photo" role="img" aria-label="Portrait photograph of the consultant in a blue plaid suit and lavender tie over an orange circle" style="left:156px;top:1151px;width:442px;height:442px;background:linear-gradient(180deg,#f08f49 0%,#ee7325 35%,#7d8fb5 36%,#6a7aa0 100%)"></div>
<h2 class="abs heading about-title">ABOUT <span class="accent">ME</span></h2>
<div class="rule" style="left:644px;top:1164px"></div>
<div class="abs about-text">
  <p>Marcus Delaney is the Owner of Meridian Project Partners, LLC and serves as Principal Lead Consultant on waterfall and agile contract opportunities.</p>
  <p>Meridian Project Partners, LLC has engaged on a contract basis with Kestrelmark 300 companies across various industries including banking and credit unions, global supply chain, and international food distribution. Marcus Delaney brings 12 years of experience ...</p>
</div>
<div class="abs stat" style="left:644px"><b>500+</b><span>Satisfied Clients</span></div>
<div class="abs stat" style="left:815px"><b>99%</b><span>Success of Works</span></div>
<div class="btn" style="left:644px;top:1542px;width:153px;height:41px">KNOW MORE</div>

<!-- certifications -->
<h2 class="abs heading center-head" style="top:1700px">CERTIFICATIONS <span class="accent">&amp; CREDENTIALS</span></h2>
<div class="rule" style="left:548px;top:1766px"></div>
<svg class="abs arrow" width="24" height="44" viewBox="0 0 24 44" style="left:158px"><path d="M20 3L4 22l16 19" fill="none" stroke="#ee7325" stroke-width="2.5"/></svg>
<svg class="abs arrow" width="24" height="44" viewBox="0 0 24 44" style="left:1018px"><path d="M4 3l16 19L4 41" fill="none" stroke="#ee7325" stroke-width="2.5"/></svg>
<svg class="abs badge-row" viewBox="0 0 780 90" role="img" aria-label="Row of six certification badges">
  <g fill="#e9f6fb">
    <circle cx="72" cy="65" r="27"/><circle cx="208" cy="23" r="27"/><circle cx="345" cy="65" r="27"/><circle cx="483" cy="23" r="27"/><circle cx="622" cy="65" r="27"/><circle cx="758" cy="23" r="27"/>
  </g>
  <g fill="#c7ebf8">
    <circle cx="40" cy="45" r="40"/><circle cx="177" cy="45" r="40"/><circle cx="315" cy="45" r="40"/><circle cx="453" cy="45" r="40"/><circle cx="591" cy="45" r="40"/><circle cx="728" cy="45" r="40"/>
  </g>
</svg>

<!-- trusted -->
<h2 class="abs heading trusted-title">TRUSTED BY BIGGEST<br><span class="accent">BUSINESS NAMES</span></h2>
<div class="rule" style="left:159px;top:2166px"></div>
<svg class="abs quote-mark" width="66" height="46" viewBox="0 0 66 46"><path d="M4 26a13 13 0 1 1 20 0l-6 18h-8l4-14A12 12 0 0 1 4 26zM36 26a13 13 0 1 1 20 0l-6 18h-8l4-14a12 12 0 0 1-10-4z" fill="#c7ebf8"/></svg>
<p class="abs quote">Lorem ipsum dolor sit amet, consectetur adipiscing elit, sed do eiusmod tempor incididunt ut labore et dolore magna aliqua. Ut enim ad minim veniam, quis nostrud exercitation ullamco laboris nisi ut aliquip ex ea commodo consequat.</p>
<div class="abs quote-name">DANA WHITFIELD</div>
<div class="abs quote-role">Brightloom Studio</div>
<svg class="abs" style="left:590px;top:1990px" width="460" height="420" viewBox="0 0 460 420">
  <circle cx="71" cy="71" r="63" fill="#f08f49"/>
  <circle cx="381" cy="331" r="70" fill="#00a9dd"/>
</svg>
<div class="photo" role="img" aria-label="Photograph of the consultant seated in an office in a striped jacket" style="left:613px;top:1998px;width:408px;height:408px;background:radial-gradient(circle at 50% 45%,#b78a6e,#6d6f78 60%,#3a3d46)"></div>

<!-- experience -->
<h2 class="abs heading center-head" style="top:2478px;color:var(--blue)">EXPERIENCE</h2>
<div class="rule" style="left:579px;top:2541px"></div>
<div class="card-img" role="img" aria-label="Photograph of the consultant in a tan setting" style="left:159px;width:267px;background:linear-gradient(160deg,#a08370,#5a4438)"></div>
<div class="card-img" role="img" aria-label="Photograph of the consultant in a blue plaid suit on white" style="left:466px;width:267px;background:linear-gradient(180deg,#f1f2f4,#8fa0c0)"></div>
<div class="card-img" role="img" aria-label="Photograph of the consultant in a pinstripe suit on black" style="left:775px;width:265px;background:linear-gradient(180deg,#2a2424,#111)"></div>
<div class="card-title" style="left:159px;width:267px">SENIOR SAFE SCRUM<br>MASTER</div>
<div class="card-title" style="left:466px;width:267px">SENIOR PROJECT<br>MANGER</div>
<div class="card-title" style="left:775px;width:265px">SENIOR PROGRAM<br>MANGER</div>

<!-- contact -->
<h2 class="abs heading contact-title">GET IN <span class="accent">TOUCH</span></h2>
<div class="rule" style="left:158px;top:3023px"></div>
<p class="abs contact-text">We're glad to discuss your organisation's situation. So please contact us via the details below, or enter your request.</p>
<div class="abs contact-line" style="top:3155px">
  <svg width="26" height="26" viewBox="0 0 26 26"><circle cx="13" cy="13" r="12" fill="none" stroke="#00a9dd" stroke-width="1.5"/><path d="M13 6a5 5 0 0 1 5 5c0 4-5 9-5 9s-5-5-5-9a5 5 0 0 1 5-5z" fill="none" stroke="#00a9dd" stroke-width="1.5"/><circle cx="13" cy="11" r="1.8" fill="#00a9dd"/></svg>
  <span class="lbl">Address -</span><span class="val">48 Alder Crest Rd,<br>NY, 10021, USA.</span>
</div>
<div class="abs contact-line" style="top:3213px">
  <svg width="26" height="26" viewBox="0 0 26 26"><circle cx="13" cy="13" r="12" fill="none" stroke="#00a9dd" stroke-width="1.5"/><path d="M9 7l2 3-1 1c.6 1.6 1.8 2.8 3.4 3.4l1-1 3 2-.8 2C11 17.5 8.5 15 8 8z" fill="none" stroke="#00a9dd" stroke-width="1.4"/></svg>
  <span class="lbl">Call Me -</span><span class="val" style="font-weight:700">(555) 010-2468</span>
</div>
<div class="abs contact-line" style="top:3247px">
  <svg width="26" height="26" viewBox="0 0 26 26"><circle cx="13" cy="13" r="12" fill="none" stroke="#00a9dd" stroke-width="1.5"/><rect x="7" y="9" width="12" height="8" fill="none" stroke="#00a9dd" stroke-width="1.3"/><path d="M7 9l6 5 6-5" fill="none" stroke="#00a9dd" stroke-width="1.3"/></svg>
  <span class="lbl">Emai Me -</span><span class="val" style="text-decoration:underline">hello@meridianpartners.example</span>
</div>

<div class="field" style="left:539px;top:2972px;width:240px;height:36px">FIRST NAME</div>
<div class="field" style="left:799px;top:2972px;width:240px;height:36px">LAST NAME</div>
<div class="field" style="left:539px;top:3028px;width:240px;height:36px">EMAIL ADDRESS</div>
<div class="field" style="left:799px;top:3028px;width:240px;height:36px">PHONE</div>
<div class="field" style="left:539px;top:3084px;width:240px;height:36px">WEBSITE</div>
<div class="field" style="left:799px;top:3084px;width:240px;height:36px">SERVICES</div>
<div class="field" style="left:539px;top:3138px;width:500px;height:102px">MESSAGE</div>
<div class="btn" style="left:857px;top:3260px;width:181px;height:41px">SEND REQUEST</div>

<!-- footer -->
<footer class="abs footer"></footer>
<div class="abs foot-head" style="left:158px;top:3440px">USEFULL LINKS</div>
<ul class="abs foot-links" style="left:158px;top:3478px;width:140px">
  <li>- About Me</li><li>- Experience</li><li style="line-height:16px;padding:4px 0">- Certifications and<br>&nbsp;&nbsp;Credentials</li><li>- Contact Us</li>
</ul>
<ul class="abs foot-links" style="left:309px;top:3478px">
  <li>- Privacy Policy</li><li>- Terms &amp; Conditions</li>
</ul>
<div class="abs foot-head" style="left:481px;top:3440px">SERVICES</div>
<ul class="abs foot-links" style="left:481px;top:3478px">
  <li>- Services1</li><li>- Services1</li><li>- Services1</li><li>- Services1</li>
</ul>
<div class="abs brand" style="left:728px;top:3446px"><div class="brand-mark"></div><div class="brand-name">MERIDIAN</div></div>
<svg class="abs" style="left:815px;top:3528px" width="124" height="20" viewBox="0 0 124 20">
  <g fill="#00a9dd">
    <circle cx="8" cy="10" r="7"/><circle cx="36" cy="10" r="7"/><circle cx="64" cy="10" r="7"/><circle cx="92" cy="10" r="7"/>
  </g>
</svg>
<div class="abs copyright">Copyright © 2022 MERIDIAN LLC. All rights reserved.</div>

</body>
</html>
```